Lantern Jubilee Flyer

I need an 8.5x11 or 8.5x14 or 11x17 flyer for a benefit concert. Logo has already been designed; uploading several different versions, and you could choose which you want to use. For flyer design: something subtly musical (not a big fan of using musical symbols in the design, treble clefs, eighth notes, etc.) But something classy. I'm uploading unformatted copy, and two logos: one of the radio station that is helping to sponsor the event, and one for the organization the concert is benefitting. This is quick turnaround, so I promise to be very responsive with feedback. Thanks!

```html
<!DOCTYPE html>
<html lang="en">
<head>
<meta charset="utf-8">
<title>Lantern Jubilee Flyer</title>
<link href="https://fonts.googleapis.com/css2?family=Anton&family=Montserrat:wght@400;700;800&display=swap" rel="stylesheet">
<style>
  :root {
    --paper: #ffffff;
    --band-yellow: #fbf500;
    --band-amber: #df9530;
    --headline-pink: #ff0a6e;
    --info-white: #ffffff;
    --note-grey: #5a5a5a;
    --sponsor-slate: #3b4650;
    --station-orange: #e4892c;
    --footer-blue: #3d86c2;
    --runner-a: #f29a2e;
    --runner-b: #e8417a;
    --runner-c: #2fae9a;
    --runner-d: #7a2f78;
    --runner-e: #c8df72;
  }
  html, body {
    margin: 0;
    padding: 0;
    overflow: hidden;
  }
  body {
    width: 927px;
    height: 1200px;
    background: var(--paper);
  }
  .flyer {
    position: relative;
    width: 927px;
    height: 1200px;
    overflow: hidden;
    background: var(--paper);
    font-family: "Montserrat", Arial, sans-serif;
  }
  .runners-art {
    position: absolute;
    left: 22px;
    top: 12px;
    width: 884px;
    height: 620px;
    border-radius: 40px 40px 0 0;
    background:
      radial-gradient(ellipse at 30% 40%, rgba(47,174,154,.55), transparent 60%),
      radial-gradient(ellipse at 75% 30%, rgba(200,223,114,.6), transparent 55%),
      linear-gradient(100deg, var(--runner-a) 0%, var(--runner-b) 35%, var(--runner-d) 55%, var(--runner-c) 70%, var(--runner-b) 100%);
    opacity: .85;
  }
  .title-bands {
    position: absolute;
    inset: 0;
  }
  .band-yellow { fill: var(--band-yellow); }
  .band-amber { fill: var(--band-amber); }
  .presenter {
    font-family: "Montserrat", Arial, sans-serif;
    font-weight: 800;
    font-size: 30px;
    fill: var(--headline-pink);
  }
  .event-title {
    font-family: "Anton", Impact, sans-serif;
    font-size: 112px;
    fill: var(--headline-pink);
  }
  .event-info {
    font-family: "Montserrat", Arial, sans-serif;
    font-weight: 400;
    font-size: 30px;
    fill: var(--info-white);
  }
  .notes {
    position: absolute;
    right: 41px;
    top: 872px;
    margin: 0;
    text-align: right;
    color: var(--note-grey);
    font-size: 27px;
    line-height: 42px;
    letter-spacing: .5px;
  }
  .notes p { margin: 0; }
  .sponsor {
    position: absolute;
    display: flex;
    align-items: center;
    gap: 12px;
    font-family: "Montserrat", Arial, sans-serif;
    font-weight: 800;
  }
  .sponsor-mark {
    flex: none;
    width: 26px;
    height: 26px;
  }
  .sponsor--beneficiary {
    left: 226px;
    top: 1030px;
    width: 270px;
    color: var(--sponsor-slate);
    font-size: 30px;
    line-height: 34px;
  }
  .sponsor--beneficiary .sponsor-mark { background: var(--sponsor-slate); }
  .sponsor--station {
    left: 536px;
    top: 1050px;
    color: var(--station-orange);
    font-size: 52px;
  }
  .sponsor--station .sponsor-mark { background: var(--station-orange); }
  .footer-bar {
    position: absolute;
    left: 0;
    bottom: 0;
    width: 927px;
    height: 33px;
    background: var(--footer-blue);
  }
</style>
</head>
<body>
<main class="flyer">
  <div class="runners-art" role="img" aria-label="Colourful faceted illustration of a group of runners in orange, pink, teal and purple"></div>

  <svg class="title-bands" width="927" height="1200" viewBox="0 0 927 1200" aria-label="Event title and details">
    <polygon class="band-yellow" points="0,729 927,496 927,685 0,908"/>
    <polygon class="band-amber" points="0,908 927,685 927,758 0,979"/>

    <text class="presenter" x="31" y="762" transform="rotate(-13.7 31 762)" textLength="300" lengthAdjust="spacingAndGlyphs">97.3 Persents</text>
    <text class="event-title" x="33" y="866" transform="rotate(-13.7 33 866)" textLength="878" lengthAdjust="spacingAndGlyphs">LANTERN JUBILEE</text>

    <text class="event-info" x="33" y="950" transform="rotate(-13.7 33 950)" textLength="338" lengthAdjust="spacingAndGlyphs">DATE :  XX-12-2017</text>
    <text class="event-info" x="409" y="862" transform="rotate(-13.7 409 862)" textLength="488" lengthAdjust="spacingAndGlyphs">VENUE : PALACE NAME ERE</text>
  </svg>

  <div class="notes">
    <p>OTHER TEXT HERE</p>
    <p>OTHER TEXT HERE</p>
  </div>

  <div class="sponsor sponsor--beneficiary">
    <span class="sponsor-mark"></span>
    <span>Midwinter Lantern Jubilee</span>
  </div>

  <div class="sponsor sponsor--station">
    <span class="sponsor-mark"></span>
    <span>97.3 KVLR</span>
  </div>

  <div class="footer-bar"></div>
</main>
</body>
</html>
```